Tallowmere Editing Services (TEServices-hub.net)

We need a Wordpress-based site designed for a client who provides writing and editing services for the IT industry. We have a wireframe complete for the homepage, but need all internal pages designed (based on homepage wireframe) and the entire site coded for WP.

Internal pages include: "Our Work" (with samples & testimonials); "Capabilities" (with sections to address "strategy", "coaching", "writing" and "editing"); "About Us"; and a Contact page.

Will provide all copywriting, writing samples, testimonials, and client logos.

We completely realize/acknowledge the subject matter is visually BORING! Anything at all that can be done to make it look visually appealing would be *great*! Stock photography is fine.

Please feel free to ask any questions whatsoever. Thanks for your time!

```html
<!DOCTYPE html>
<html lang="en">
<head>
<meta charset="utf-8">
<title>Tallowmere Editing Services</title>
<link href="https://fonts.googleapis.com/css2?family=Nunito:wght@400;600;700;800;900&family=Nunito+Sans:wght@400;600;700&display=swap" rel="stylesheet">
<style>
:root{
  --primary:#6454e8;
  --navy:#2e2a62;
  --text:#4a4a5e;
  --band:#f3f4fd;
  --field:#eef4f8;
  --footer-bar:#2f2b5e;
}
*{box-sizing:border-box;margin:0;padding:0}
html,body{width:1200px;height:4609px;overflow:hidden;background:#fff}
body{position:relative;font-family:"Nunito Sans",sans-serif;color:var(--text)}
.abs{position:absolute}
h1,h2,h3,.brand{font-family:"Nunito",sans-serif;color:var(--navy);font-weight:800}
.dot{color:var(--primary)}
.btn{position:absolute;display:flex;align-items:center;justify-content:center;background:var(--primary);color:#fff;font-size:11px;font-weight:700;border-radius:2px;letter-spacing:.3px}
.photo{position:absolute}

/* header */
.brand{position:absolute;left:73px;top:36px;font-size:20px;font-weight:700}
.nav{position:absolute;left:400px;top:35px;display:flex;gap:26px;font-size:14px;font-weight:700;color:var(--navy);font-family:"Nunito",sans-serif}
.nav .active{color:var(--primary)}

/* hero */
.hero-title{left:125px;top:196px;font-size:42px;line-height:46px;white-space:nowrap}
.hero-text{left:125px;top:316px;font-size:15px;line-height:27px;width:360px}
.link-more{left:261px;top:403px;font-size:11px;font-weight:700;color:var(--primary)}
.hero-photo{left:800px;top:85px;width:380px;height:470px;border-radius:46% 54% 40% 60% / 40% 46% 54% 60%;background:linear-gradient(140deg,#d9d3cb,#b59f8c 60%,#e39a3c)}

/* section heads */
.sec-title{left:0;width:1200px;text-align:center;font-size:36px}
.sec-sub{left:0;width:1200px;text-align:center;font-size:13px;line-height:21px}

/* services */
.card{position:absolute;top:805px;width:205px;height:288px;background:#fff;box-shadow:0 4px 18px rgba(40,40,90,.08);text-align:center}
.card svg{margin-top:42px}
.card h3{font-size:18px;margin-top:20px}
.card p{font-size:12.5px;line-height:21px;margin:22px auto 0;width:150px}

/* clients */
.client{position:absolute;top:1412px;font-family:"Nunito",sans-serif;font-weight:800;font-size:18px;color:#6e6e78;display:flex;align-items:center;gap:8px}
.client i{display:inline-block;width:14px;height:14px;background:#6e6e78;border-radius:50%}

/* focus */
.focus-photo{left:0;top:1625px;width:480px;height:470px;border-radius:0 60% 55% 0 / 0 50% 60% 40%;background:linear-gradient(140deg,#5a4a42,#b0a08f 55%,#d8cbbd)}
.focus-title{left:650px;top:1762px;font-size:36px;line-height:42px}
.focus-text{left:650px;top:1876px;width:430px;font-size:12.5px;line-height:22px}

/* portfolio */
.tile{position:absolute;top:2460px;width:276px;height:267px}
.pager{position:absolute;top:2768px;left:570px;display:flex;gap:6px}
.pager span{width:10px;height:10px;border-radius:50%;background:#ddd}
.pager span:first-child{background:var(--primary)}

/* testimonials */
.band{position:absolute;left:0;top:2920px;width:1200px;height:570px;background:var(--band)}
.quote{position:absolute;top:3142px;width:472px;height:258px;background:#fff;padding:34px 34px}
.stars{color:var(--primary);font-size:14px;letter-spacing:1px}
.quote p{margin-top:12px;font-size:13px;line-height:22px;width:410px}
.who{display:flex;align-items:center;gap:18px;margin-top:36px}
.avatar{width:56px;height:56px;border-radius:50%;background:linear-gradient(135deg,#7a5a4a,#d4b49c)}
.who b{display:block;font-family:"Nunito",sans-serif;font-size:18px;color:var(--navy);font-weight:800;white-space:nowrap}
.who small{font-size:13px;color:var(--navy)}

/* contact */
.contact-photo{left:60px;top:3600px;width:520px;height:490px;border-radius:40% 60% 55% 45% / 35% 50% 60% 60%;background:linear-gradient(140deg,#c9c3bd,#8a7f78 55%,#4c5a4a)}
.contact-title{left:683px;top:3628px;font-size:36px}
.contact-text{left:683px;top:3695px;width:400px;font-size:12.5px;line-height:22px}
.field{position:absolute;background:var(--field);font-size:12px;color:#a0a8b4;padding:16px 16px}

/* footer */
.footer{position:absolute;left:0;top:4230px;width:1200px;height:325px;background:var(--band)}
.foot-brand{left:138px;top:4295px;font-size:22px}
.foot-text{left:138px;top:4342px;font-size:14px;line-height:30px;color:var(--navy)}
.newsletter{left:138px;top:4433px;width:290px;height:42px;background:#fff;box-shadow:0 3px 12px rgba(40,40,90,.08);font-size:12px;color:var(--navy);padding:13px 16px}
.social{position:absolute;left:835px;top:4362px;display:flex;gap:18px;font-family:"Nunito",sans-serif;font-weight:800;font-size:14px;color:var(--primary)}
.copyright{position:absolute;left:0;top:4555px;width:1200px;height:54px;background:var(--footer-bar);color:#fff;text-align:center;font-size:14px;font-weight:600;line-height:54px}
</style>
</head>
<body>

<!-- header -->
<div class="brand">Tallowmere Editing Services</div>
<nav class="nav"><span class="active">Home</span><span>Our Woks</span><span>Capabilities</span><span>About Us</span><span>Blogs</span></nav>
<div class="btn" style="left:989px;top:19px;width:136px;height:48px">Get in touch</div>

<!-- hero -->
<h1 class="abs hero-title">Communicate your expertise<br>&amp; customer succeses</h1>
<p class="abs hero-text">We understand that businesses need good communication, that we are now</p>
<div class="btn" style="left:125px;top:386px;width:113px;height:49px">HIRE US</div>
<span class="abs link-more">LEARN MORE</span>
<div class="photo hero-photo" role="img" aria-label="Photo collage of a man working at a desk and hands writing in a notebook beside a laptop"></div>

<!-- services -->
<h2 class="abs sec-title" style="top:672px">Services that we provide<span class="dot">.</span></h2>
<p class="abs sec-sub" style="top:737px">Text copy that explains in concice, snappy terms the value you provide to<br>customers</p>
<div class="card" style="left:125px"><svg width="62" height="58" viewBox="0 0 62 58"><ellipse cx="31" cy="30" rx="28" ry="26" fill="#7fd3e8"/><circle cx="31" cy="25" r="9" fill="none" stroke="#2e2a62" stroke-width="2"/><rect x="27" y="34" width="8" height="8" fill="none" stroke="#2e2a62" stroke-width="2"/></svg><h3>Strategy</h3><p>Nam libero tempore, cum soluta nobis est eligendi optio cumque.</p></div>
<div class="card" style="left:362px"><svg width="62" height="58" viewBox="0 0 62 58"><ellipse cx="31" cy="30" rx="28" ry="26" fill="#f7944a"/><rect x="19" y="18" width="24" height="18" fill="none" stroke="#2e2a62" stroke-width="2"/><line x1="17" y1="42" x2="45" y2="42" stroke="#2e2a62" stroke-width="2"/></svg><h3>Coaching</h3><p>Nam libero tempore, cum soluta nobis est eligendi optio cumque.</p></div>
<div class="card" style="left:600px"><svg width="62" height="58" viewBox="0 0 62 58"><ellipse cx="31" cy="30" rx="28" ry="26" fill="#8b95e6"/><rect x="21" y="16" width="20" height="26" fill="#fff" stroke="#2e2a62" stroke-width="2"/><line x1="25" y1="24" x2="37" y2="24" stroke="#2e2a62" stroke-width="2"/><line x1="25" y1="30" x2="37" y2="30" stroke="#2e2a62" stroke-width="2"/></svg><h3>Writting</h3><p>Nam libero tempore, cum soluta nobis est eligendi optio cumque.</p></div>
<div class="card" style="left:837px"><svg width="62" height="58" viewBox="0 0 62 58"><ellipse cx="31" cy="30" rx="28" ry="26" fill="#ffe27a"/><rect x="18" y="18" width="10" height="24" fill="none" stroke="#2e2a62" stroke-width="2"/><rect x="30" y="30" width="14" height="12" fill="none" stroke="#2e2a62" stroke-width="2"/></svg><h3>Editing</h3><p>Nam libero tempore, cum soluta nobis est eligendi optio cumque.</p></div>

<!-- clients -->
<h2 class="abs sec-title" style="top:1218px;font-size:34px">Our Current and Past Clients</h2>
<div class="client" style="left:140px"><i></i>Parlo</div>
<div class="client" style="left:290px">Verdane</div>
<div class="client" style="left:460px">Ledgerline</div>
<div class="client" style="left:635px">Counselry</div>
<div class="client" style="left:815px">Mosswick</div>
<div class="client" style="left:985px"><i></i>Orbitly</div>

<!-- focus -->
<div class="photo focus-photo" role="img" aria-label="Photo of two colleagues reviewing work together at a laptop"></div>
<h2 class="abs focus-title">We focus on digital<br>design solutions</h2>
<p class="abs focus-text">At vero eos et accusamus et iusto odio dignissimos ducimus qui blanditiis praesentium voluptatum deleniti atque corrupti quos dolores et quas molestias excepturi sint occaecati cupiditate non provident, similique sunt in culpa qui officia deserunt.</p>
<div class="btn" style="left:650px;top:1980px;width:126px;height:47px">ABOUT US</div>

<!-- portfolio -->
<h2 class="abs sec-title" style="top:2302px;line-height:44px">Text highlighting the<br>type of work you do<span class="dot">.</span></h2>
<p class="abs sec-sub" style="top:2410px">Here are some of our portfolios for our clients</p>
<div class="tile" role="img" aria-label="Photo of a designer editing a portrait on a desktop monitor" style="left:12px;background:linear-gradient(135deg,#5b6a48,#6fb0d8)"></div>
<div class="tile" role="img" aria-label="Photo of a video editing workstation with monitors" style="left:312px;background:linear-gradient(135deg,#6f7c84,#c9c9c4)"></div>
<div class="tile" role="img" aria-label="Photo of hands pointing at charts on a tablet" style="left:612px;background:linear-gradient(135deg,#d5d9dd,#8fb8c2)"></div>
<div class="tile" role="img" aria-label="Photo of friends looking at phones against a pink wall" style="left:912px;background:linear-gradient(135deg,#f3c9b5,#8b6e6a)"></div>
<div class="pager"><span></span><span></span><span></span><span></span></div>

<!-- testimonials -->
<div class="band"></div>
<h2 class="abs sec-title" style="top:3015px">Happy clients say</h2>
<p class="abs sec-sub" style="top:3078px">Nam libero tempore, cum soluta nobis est eligendi optio cumque nihil<br>impedit quo minus id quod maxime placeat facere.</p>
<div class="quote" style="left:0"><div class="stars">★★★★★</div><p>Nam libero tempore, cum soluta nobis est eligendi optio cumque nihil impedit quo minus id quod maxime placeat facere possimus, omnis voluptas assumenda.</p><div class="who"><div class="avatar" role="img" aria-label="Client portrait"></div><div><b>Marisol Quade</b><small>Product Designer</small></div></div></div>
<div class="quote" style="left:488px"><div class="stars">★★★★★</div><p>Nam libero tempore, cum soluta nobis est eligendi optio cumque nihil impedit quo minus id quod maxime placeat facere possimus, omnis voluptas assumenda.</p><div class="who"><div class="avatar" role="img" aria-label="Client portrait"></div><div><b>Teodor Hale</b><small>Customer Support</small></div></div></div>
<div class="quote" style="left:977px"><div class="stars">★★★★★</div><p>Nam libero tempore, cum soluta nobis est eligendi optio cumque nihil impedit quo minus id quod maxime placeat facere possimus, omnis voluptas assumenda.</p><div class="who"><div class="avatar" role="img" aria-label="Client portrait"></div><div><b>Priya Lennart</b><small>Web Developer</small></div></div></div>

<!-- contact -->
<div class="photo contact-photo" role="img" aria-label="Photo of a smiling support agent wearing a headset"></div>
<h2 class="abs contact-title">Contact us</h2>
<p class="abs contact-text">At vero eos et accusamus et iusto odio dignissimos ducimus qui blanditiis praesentium voluptatum deleniti atque corrupti.</p>
<div class="field" style="left:683px;top:3765px;width:190px;height:48px">Name*</div>
<div class="field" style="left:885px;top:3765px;width:190px;height:48px">Email*</div>
<div class="field" style="left:683px;top:3828px;width:190px;height:48px">Phone*</div>
<div class="field" style="left:885px;top:3828px;width:190px;height:48px">Select*</div>
<div class="field" style="left:683px;top:3890px;width:392px;height:165px">Message*</div>
<div class="btn" style="left:800px;top:4075px;width:160px;height:47px">Submit Message</div>

<!-- footer -->
<div class="footer"></div>
<div class="abs brand foot-brand">Tallowmere Editing Services</div>
<p class="abs foot-text">48 Larchmoor Row, Eastbury, Wrenfield.<br>(555) 0142 3318 | M: hello@teservices-hub.net</p>
<div class="abs newsletter">Subscribe to Our Newsletter</div>
<div class="social"><span>Chatterly</span><span>Proline</span><span>Vidstream</span><span>Snapframe</span></div>
<div class="copyright">Copyright (c) Tallowmere Editing Services 2021. All right reserved.</div>

</body>
</html>
```